Stylish, Masculine Design - Men's Clothing

Granary Coat Mart is a 14,000 square foot warehouse outlet store open to the public since 2005. 50+ brands. Well-known designer brand names and private labels. 30-80% off retail everyday. Lowest prices guaranteed. Average suit price $150. Average shirt price $20. One-stop shop shopping. Men's suits, tuxedos, tuxedo rentals, dress shirts, ties, dress shoes, boy's suits and tuxedos, clergy robes, clergy shirts, cologne, loungewear. Slim fits (Prom Dance), business styles, "church" fashion, security-related uniform. Alterations done by expert tailors on premises for an extra charge.
The final design for both business card and logo should portray stylishness and masculinity.
Updates
We will be changing our name. Details below.New name: Warehouse Suit & TuxFormer name: Granary Coat Mart Added Monday, December 26, 2016
Target Market(s)
Gender: 80% Male, 15% Female, 5% Transgender
Location: 80% 10 Mile Radius, 20% >10 Mile Radius
Age: 17-18 (Primarily prom), 18-35 (Primarily Interviews and Weddings), 36-70 (primarily Church and events)
Race: African-American 50%, Latino-American 20%, White 15%, 10% Asian 5% Other
Religions: Christian 50%, 20% Catholic, 10% Mormon, 20% Other/None
Occupation: Local government 40%, Large corporation employee 20%, Small business employee 10%, Small business owner 10%, 20% Unemployed (high school, college)
Education: High School or equivalent 40%, College 30%, Some College 20%, Masters/Doctors 10%
Industry/Entity Type
Retail
Contact Information for Business Card
Name: Peter Olund
Title: Sales Associate
Address: 418 E. Mirabeth Ave. Gardena, CA 90247
Phone Number: 310.555.0182
Slogan: Warehouse Selection. Outlet Prices, Outstanding Service
www.granarycoatmart.example
Logo Text
GCM (Acronym for Granary Coat Mart) or Image
Requirements
Must have
- Easy to read
- Visually appealing

```html
<!DOCTYPE html>
<html lang="en">
<head>
<meta charset="utf-8">
<title>Granary Coat Mart – Business Card</title>
<link rel="stylesheet" href="https://fonts.googleapis.com/css2?family=Oswald:wght@400;500&family=Montserrat:wght@400;700&family=Merriweather:wght@400&family=Open+Sans:wght@400&display=swap">
<style>
  :root {
    --backdrop: #3b3431;
    --card-black: #151515;
    --card-white: #ffffff;
    --ink: #1a1a1a;
    --paper-text: #f2f2f2;
    --accent-red: #d9252f;
    --slogan-red: #e0505a;
    --rule: #222222;
  }
  * { margin: 0; padding: 0; box-sizing: border-box; }
  html, body {
    width: 1200px; height: 818px; overflow: hidden;
    background: var(--backdrop);
  }
  .canvas {
    position: relative; width: 1200px; height: 818px;
  }
  .card {
    position: absolute; top: 255px;
    width: 540px; height: 308px;
  }
  .card--front {
    left: 45px; background: var(--card-black);
    display: flex; flex-direction: column; align-items: center; justify-content: center;
  }
  .card--back {
    left: 615px; background: var(--card-white);
    display: flex; align-items: center;
  }
  .wordmark {
    font-family: "Oswald", sans-serif; font-weight: 500;
    text-transform: uppercase; line-height: 0.95; text-align: center;
  }
  .card--front .wordmark {
    color: var(--paper-text); font-size: 54px;
  }
  .slogan {
    margin-top: 16px;
    font-family: "Oswald", sans-serif; font-weight: 400;
    text-transform: uppercase; font-size: 17px; letter-spacing: 0.5px;
    color: var(--slogan-red);
  }
  .back-brand {
    width: 228px; padding-left: 28px;
  }
  .card--back .wordmark {
    color: var(--ink); font-size: 40px; text-align: left;
  }
  .divider {
    width: 2px; height: 150px; background: var(--rule); margin: 0 20px 0 6px;
  }
  .details { flex: 1; }
  .person-name {
    font-family: "Montserrat", sans-serif; font-size: 21px; color: var(--ink);
    font-weight: 400;
  }
  .person-name strong { font-weight: 700; }
  .person-title {
    font-family: "Merriweather", serif; font-size: 14px; color: var(--accent-red);
    margin-bottom: 14px;
  }
  .contact-list { list-style: none; }
  .contact-item {
    display: flex; align-items: center; gap: 8px;
    font-family: "Open Sans", sans-serif; font-size: 12.5px; color: var(--ink);
    margin-bottom: 5px; white-space: nowrap;
  }
  .contact-item svg { width: 12px; height: 12px; flex: none; fill: var(--accent-red); }
</style>
</head>
<body>
<main class="canvas">
  <section class="card card--front">
    <div class="wordmark">Granary<br>Coat Mart</div>
    <p class="slogan">Outlet Prices, Outstanding Service</p>
  </section>

  <section class="card card--back">
    <div class="back-brand">
      <div class="wordmark">Granary<br>Coat Mart</div>
    </div>
    <div class="divider"></div>
    <div class="details">
      <h1 class="person-name">Peter <strong>Olund</strong></h1>
      <p class="person-title">Sales Associate</p>
      <ul class="contact-list">
        <li class="contact-item">
          <svg viewBox="0 0 12 12" aria-hidden="true"><path d="M6 0a4 4 0 0 0-4 4c0 3 4 8 4 8s4-5 4-8a4 4 0 0 0-4-4zm0 5.6A1.6 1.6 0 1 1 6 2.4a1.6 1.6 0 0 1 0 3.2z"/></svg>
          418 E. Mirabeth Ave. Gardena, CA 90247
        </li>
        <li class="contact-item">
          <svg viewBox="0 0 12 12" aria-hidden="true"><path d="M1 3.5C1 2 3 1.5 6 1.5s5 .5 5 2v1H8.5V3.6h-5v.9H1zM3 5.5h6l1.5 5h-9z"/></svg>
          310.555.0182
        </li>
        <li class="contact-item">
          <svg viewBox="0 0 12 12" aria-hidden="true"><path d="M1 2.5h10v7H1zm.8.8L6 6.4l4.2-3.1z"/></svg>
          www.granarycoatmart.example
        </li>
      </ul>
    </div>
  </section>
</main>
</body>
</html>
```